Design some Business Cards for Brindle Office Assistance

Hello Everyone! I need a business card designed. I have attached the logo and the color scheme can be found on my website at www.brindleofficehelp.com (teal as the primary color). I look forward to seeing your ideas!

```html
<!DOCTYPE html>
<html lang="en">
<head>
<meta charset="utf-8">
<title>Brindle Office Assistance – Business Card</title>
<link href="https://fonts.googleapis.com/css2?family=Handlee&display=swap" rel="stylesheet">
<style>
  :root {
    --page-bg: #e6e3df;
    --card-bg: #f1e9e0;
    --teal: #46ab9d;
    --navy: #1f2a6b;
    --white: #ffffff;
    --illustration-tone: #b9d6cf;
  }
  * { margin: 0; padding: 0; box-sizing: border-box; }
  html, body {
    width: 1200px;
    height: 848px;
    overflow: hidden;
    background: var(--page-bg);
  }
  .canvas {
    position: relative;
    width: 1200px;
    height: 848px;
  }
  .business-card {
    position: absolute;
    left: 75px;
    top: 125px;
    width: 1050px;
    height: 597px;
    background: var(--card-bg);
    overflow: hidden;
    box-shadow: 0 4px 18px rgba(0, 0, 0, 0.12);
  }
  .wave-ribbons {
    position: absolute;
    left: 0;
    top: 250px;
    width: 1050px;
    height: 146px;
    background: linear-gradient(100deg,
      rgba(127, 182, 216, 0.15) 0%,
      rgba(217, 214, 90, 0.55) 35%,
      rgba(201, 74, 92, 0.5) 60%,
      rgba(127, 182, 216, 0.6) 85%,
      rgba(227, 154, 74, 0.5) 100%);
  }
  .assistant-illustration {
    position: absolute;
    left: 130px;
    top: 14px;
    width: 300px;
    height: 382px;
    background: var(--illustration-tone);
  }
  .brand-name {
    position: absolute;
    left: 460px;
    top: 112px;
    font-family: "Handlee", cursive;
    font-size: 37px;
    font-weight: 400;
    color: var(--navy);
    white-space: nowrap;
  }
  .brand-underline {
    position: absolute;
    left: 450px;
    top: 150px;
  }
  .contact-band {
    position: absolute;
    left: 0;
    top: 396px;
    width: 1050px;
    height: 201px;
    background: var(--teal);
  }
  .contact-item {
    position: absolute;
    display: flex;
    align-items: center;
    gap: 12px;
    font-family: "Handlee", cursive;
    font-size: 31px;
    color: var(--white);
    white-space: nowrap;
    transform: translateY(-50%);
  }
  .contact-icon {
    width: 36px;
    height: 36px;
    flex: none;
  }
  .social-square {
    width: 34px;
    height: 34px;
    flex: none;
    background: var(--white);
    border-radius: 4px;
  }
  .col-left { left: 20px; }
  .col-right { left: 508px; }
  .row-1 { top: 54px; }
  .row-2 { top: 106px; }
  .row-3 { top: 157px; }
</style>
</head>
<body>
<main class="canvas">
  <section class="business-card">
    <div class="wave-ribbons" role="img" aria-label="Flowing colourful ribbon waves in blue, yellow, red and orange"></div>
    <div class="assistant-illustration" role="img" aria-label="Cartoon illustration of a friendly office assistant holding a globe"></div>

    <h1 class="brand-name">Brindle Office Assistance</h1>
    <svg class="brand-underline" width="400" height="24" viewBox="0 0 400 24" aria-hidden="true">
      <path d="M2 20 Q120 4 392 8" fill="none" stroke="var(--navy)" stroke-width="1.6" stroke-linecap="round"/>
    </svg>

    <div class="contact-band">
      <p class="contact-item col-left row-1">
        <svg class="contact-icon" viewBox="0 0 36 36" aria-hidden="true">
          <g fill="none" stroke="var(--white)" stroke-width="2">
            <circle cx="18" cy="18" r="15"/>
            <ellipse cx="18" cy="18" rx="6.5" ry="15"/>
            <line x1="3" y1="18" x2="33" y2="18"/>
            <path d="M6 10 H30 M6 26 H30"/>
          </g>
        </svg>
        brindleofficehelp.com
      </p>
      <p class="contact-item col-left row-2"><span class="social-square"></span>#brindleofficehelp</p>
      <p class="contact-item col-left row-3"><span class="social-square"></span>#+Brindleofficehelp</p>

      <p class="contact-item col-right row-1"><span class="social-square"></span>#brindle-office-assistance</p>
      <p class="contact-item col-right row-2"><span class="social-square"></span>#brindleoffice</p>
      <p class="contact-item col-right row-3">
        <svg class="contact-icon" viewBox="0 0 36 36" aria-hidden="true">
          <rect x="2" y="8" width="32" height="21" rx="2" fill="var(--white)"/>
          <path d="M3 9 L18 21 L33 9" fill="none" stroke="var(--teal)" stroke-width="2"/>
        </svg>
        info@brindleofficehelp.com
      </p>
    </div>
  </section>
</main>
</body>
</html>
```